Electrical needs letterhead design

Need a letterhead design for an electrical company. Using the same colours as to what are used in the logo.
After a modern design.

Want the logo in top right or top left.

Must include...

ABN 71 804 239 356
PHONE 0458203917
www.kelmaroo.com.au
jed@kelmaroo.com.au

'ABN' and 'PHONE' in bold.

Keep it basic. Logo top left, details either next to it or far right corner. Dont want any other objects included.

Electrical

```html
<!DOCTYPE html>
<html lang="en">
<head>
<meta charset="utf-8">
<title>Kelmaroo Letterhead</title>
<link rel="stylesheet" href="https://fonts.googleapis.com/css2?family=Open+Sans:wght@600;700&family=Lora:wght@400;700&display=swap">
<style>
  :root {
    --backdrop: #3a2418;
    --paper: #ffffff;
    --brand-red: #b3141c;
    --brand-red-bright: #e0161c;
    --ink: #2b2b2b;
    --slate: #5b6a66;
    --rule: #444444;
  }
  * { margin: 0; padding: 0; box-sizing: border-box; }
  html, body {
    width: 954px; height: 1200px; overflow: hidden;
    background: var(--backdrop);
  }
  .letterhead {
    position: absolute; left: 40px; top: 35px;
    width: 874px; height: 1130px;
    background: var(--paper);
  }
  .brand-name {
    position: absolute; left: 30px; top: 58px;
    font-family: "Open Sans", sans-serif; font-weight: 600;
    font-size: 56px; line-height: 1; letter-spacing: -1px;
    color: var(--brand-red);
  }
  .contact {
    position: absolute; left: 629px; top: 33px;
    border-left: 1.5px solid var(--rule);
    padding: 1px 0 4px 14px;
    list-style: none;
    font-family: "Lora", serif; font-size: 15px; line-height: 23.5px;
    color: var(--ink);
  }
  .contact .label { color: var(--brand-red); font-weight: 700; margin-right: 4px; }
  .abn {
    position: absolute; left: 22px; top: 1086px;
    font-family: "Open Sans", sans-serif; font-weight: 700;
    font-size: 20px; color: var(--ink);
  }
  .footer-bands { position: absolute; left: 0; bottom: 0; }
  .footer-tag {
    position: absolute; left: 449px; top: 1094px;
    font-family: "Open Sans", sans-serif; font-weight: 700;
    font-size: 19px; letter-spacing: 3.2px; color: #ffffff;
  }
</style>
</head>
<body>
  <main class="letterhead">
    <div class="brand-name">Kelmaroo</div>

    <ul class="contact">
      <li><span class="label">P:</span>0458203917</li>
      <li><span class="label">E:</span>jed@kelmaroo.com.au</li>
      <li><span class="label">W:</span>www.kelmaroo.com.au</li>
    </ul>

    <p class="abn">ABN 71 804 239 356</p>

    <svg class="footer-bands" width="874" height="45" viewBox="0 0 874 45" aria-hidden="true">
      <defs>
        <linearGradient id="red-band" x1="0" y1="0" x2="1" y2="0">
          <stop offset="0" stop-color="#9c0d12"/>
          <stop offset="1" stop-color="#e0161c"/>
        </linearGradient>
      </defs>
      <polygon points="0,26 388,26 370,45 0,45" fill="var(--slate)"/>
      <polygon points="430,4 874,4 874,45 365,45" fill="url(#red-band)"/>
    </svg>
    <p class="footer-tag">ELECTRICAL SOLUTIONS</p>
  </main>
</body>
</html>
```